Business Podcaster needs a sexy book cover design for upcoming book launch

I'm launching a book called Find Your Mentor: how to accelerate your growth through reaching out, getting a response from, and leaving an impression on the people you admire most. It would be cool to have maybe a band of heroes or a single hero or something on the cover, then I'll need the spine designed, as well as the back cover which would be mostly just quotes about the book from other prominent people.

I dont want to extend it. I want to shorten it. Can I do that?

```html
<!DOCTYPE html>
<html lang="en">
<head>
<meta charset="utf-8">
<title>Find Your Mentor – Full Cover Wrap</title>
<link rel="stylesheet" href="https://fonts.googleapis.com/css2?family=Bebas+Neue&family=Oswald:wght@300;500&family=Raleway:wght@300&display=swap">
<style>
  :root {
    --page-bg: #f2f2f2;
    --cover-black: #000000;
    --ink-white: #ffffff;
    --art-light: #ffffff;
    --art-mid: #d9d9d9;
  }
  * { margin: 0; padding: 0; box-sizing: border-box; }
  html, body {
    width: 899px; height: 1200px; overflow: hidden;
    background: var(--page-bg);
  }
  .cover-wrap {
    position: absolute; left: 12px; top: 296px;
    width: 875px; height: 607px;
    background: var(--cover-black);
    overflow: hidden;
    color: var(--ink-white);
  }

  /* Back cover */
  .back-copy {
    position: absolute; left: 37px; top: 40px; width: 330px;
    font-family: "Oswald", sans-serif; font-weight: 500;
    font-size: 8.4px; line-height: 13.2px; text-transform: uppercase;
    text-align: justify;
  }
  .back-copy p + p { margin-top: 13px; }
  .barcode-box {
    position: absolute; left: 258px; top: 492px;
    width: 107px; height: 68px;
    background: var(--ink-white);
  }

  /* Spine */
  .spine-title, .spine-author {
    position: absolute; writing-mode: vertical-rl; transform: rotate(180deg);
    white-space: nowrap; line-height: 1;
  }
  .spine-title {
    left: 421px; top: 34px; height: 256px;
    font-family: "Bebas Neue", sans-serif; font-size: 44px;
    text-align: right;
  }
  .spine-author {
    left: 433px; top: 311px; height: 202px;
    font-family: "Raleway", sans-serif; font-weight: 300;
    font-size: 14px; letter-spacing: 9px; text-transform: uppercase;
  }
  .spine-art {
    position: absolute; left: 417px; top: 528px;
    width: 43px; height: 43px;
    background: linear-gradient(135deg, var(--art-light), var(--art-mid));
  }

  /* Front cover */
  .front-author {
    position: absolute; left: 501px; top: 18px; width: 350px;
    font-family: "Raleway", sans-serif; font-weight: 300;
    font-size: 32px; letter-spacing: 9px; line-height: 1;
    text-transform: uppercase; white-space: nowrap;
  }
  .hero-art {
    position: absolute; left: 501px; top: 146px;
    width: 160px; height: 138px;
    background: linear-gradient(135deg, var(--art-light), var(--art-mid));
  }
  .title-main, .title-sub {
    position: absolute; right: 26px; text-align: right;
    font-family: "Bebas Neue", sans-serif; font-weight: 400;
    line-height: 1; white-space: nowrap;
  }
  .title-main { top: 272px; font-size: 176px; }
  .title-sub { top: 424px; font-size: 72px; }
  .front-subtitle {
    position: absolute; right: 26px; top: 497px; text-align: right;
    font-family: "Oswald", sans-serif; font-weight: 300;
    font-size: 15px; line-height: 21.6px; text-transform: uppercase;
    white-space: nowrap;
  }
</style>
</head>
<body>
  <main class="cover-wrap">
    <section class="back-cover">
      <div class="back-copy">
        <p>Lorem ipsum dolor sit amet, consectetur adipiscing elit. Vivamus eget purus nec orci rhoncus ornare vitae sit amet odio. Donec lacinia sagittis cursus. Sed nec libero congue, porta nisl eget, aliquam nibh. Pellentesque porta quam ac metus accumsan fermentum. Vivamus faucibus fringilla purus eu sagittis. Morbi nec mollis neque. Nunc vitae dignissim ipsum, sed venenatis dolor. Nunc mattis velit id eros tristique, ut aliquam turpis vestibulum. Nam porta nec nisl quis consectetur.</p>
        <p>Curabitur efficitur volutpat magna eget ullamcorper. Quisque massa magna, scelerisque sit amet nibh vitae, iaculis rhoncus lectus. Integer in ante pharetra, finibus velit eget, bibendum orci. In enim odio, feugiat in nisi sed, semper commodo ante. Duis in malesuada purus. Curabitur fermentum egestas urna quis volutpat. Proin cursus ligula eu arcu sodales condimentum. Vivamus ac volutpat tortor, vitae maximus velit. Proin aliquet volutpat augue sed finibus. Morbi semper, mauris nec condimentum mollis, metus quam vehicula magna, sodales aliquet lectus augue nec mauris. Vestibulum ante ipsum primis in faucibus orci luctus et ultrices posuere cubilia curae; Quisque eget elementum leo, eu ultrices libero. Mauris lorem risus, interdum eget metus eu, pharetra pulvinar nisl.</p>
      </div>
      <div class="barcode-box"></div>
    </section>

    <section class="spine">
      <div class="spine-title">Find Your Mentor</div>
      <div class="spine-author">Author Name</div>
      <div class="spine-art" role="img" aria-label="Small emblem of a caped hero on a pedestal in front of a white moon"></div>
    </section>

    <section class="front-cover">
      <div class="front-author">Author Name</div>
      <div class="hero-art" role="img" aria-label="Caped hero silhouette standing on a pedestal in front of a large white moon"></div>
      <h1 class="front-title">
        <span class="title-main">Find</span>
        <span class="title-sub">Your Mentor</span>
      </h1>
      <p class="front-subtitle">How to accelerate your growth<br>through reaching out, getting a response from,<br>and leaving an impression on the people you admire most</p>
    </section>
  </main>
</body>
</html>
```